I am planning to launch a new online company called allphonedeskhub.net. This will be a place where people who work in call centres can come and purchase downloadable templates, tool-kits, courseware etc to help them in their jobs. The site will also share the latest information around research, best practices, news in the industry. Essentially a hub for everything call centre related.

I need someone to build the site for me from scratch (I have only just bought the domain name). Everything from the look and feel of the website (focus on easy to use, clean and sharp graphics, with a bit of fun), highly focused on social media and building a community, full blown e-commerce that allows for memberships/subscriptions/and one off purchase models. If you can also design custom graphics (high quality) that would be even better. Given my research of other companies in this space their websites are very dull that look like knowledge bases. I will want alot of cool visuals that attract the customers in. My initial thinking on colour scheme is bright greens/pinks/yellows etc. Not fluorescent though!

The site will contain alot of documents, templates, presentations, videos, articles, white papers etc. You must have experience in the best way to structure the site in an organised manner so that my customer can find what they need very easily.

The person who takes on this work must be happy to work collaboratively with me. It is also key that when the project is delivered that I am able to maintain alot of it myself in terms of uploading documents, blog updates, adding new products, real-time reports/analytics etc.

Whilst you are designing the website I will be working on the content so I will need your help to understand how I structure my content so that it makes sense for the design.

I will base my choice of designer on levels of experience (I will want to see previous work that you have done). I am not adverse to you using tools like shopify etc. if it meets the overall requirements of the site and adds to the functionality/look and feel.

Target Market(s)

People who work in call centres primarily those that are responsible for managing teams of the call centre itself

Industry/Entity Type

Business

Number of Pages Required

5+ page

Font styles to use
Sans Serif

Colors
33b8a4
34a6d7
886aae
b868aa
e667a6
f04a51
f68e4e
faa54b
ffcf3e

Requirements
Must have
• E-commerce functionality that allows for subscriptions and one-off payments
• Credit card processing and accept wire/bank transfers
• Easy to use layout
• Products sold alone and/or as part of bundles
• Membership area
• Front page
• About Us page
• Contact Us page
• Store page (with e-commerce back end)
• News page
• Free Resources page
• Cool, bright, fun look and feel
Nice to have
• Cool, bright, fun graphics
Should not have
• Should not look old fashioned or be difficult to navigate
• Should not look too busy or disorganised

```html
<!DOCTYPE html>
<html lang="en">
<head>
<meta charset="utf-8">
<title>allphonedeskhub.net — Home</title>
<link href="https://fonts.googleapis.com/css2?family=Montserrat:wght@300;400;500;700&display=swap" rel="stylesheet">
<style>
:root{
  --teal:#33b8a4;
  --blue:#34a6d7;
  --purple:#886aae;
  --pink:#cc64a9;
  --rose:#e667a6;
  --red:#f04a51;
  --orange:#f68e4e;
  --yellow:#ffcf3e;
  --dark-teal:#1f4a45;
  --ink:#333;
  --muted:#666;
  --line:#e4e4e4;
  --panel:#efefef;
  --panel-alt:#f6f6f6;
  --footer:#111;
}
*{box-sizing:border-box;margin:0;padding:0}
html,body{width:1200px;height:2299px;overflow:hidden;background:#fff}
body{font-family:"Montserrat",Arial,sans-serif;color:var(--ink);position:relative}
.abs{position:absolute}
.btn{position:absolute;display:flex;align-items:center;justify-content:center;font-size:11.5px;font-weight:700;letter-spacing:.3px;text-transform:uppercase;background:#fff}

/* header */
.site-header{position:absolute;left:0;top:0;width:1200px;height:141px;border-bottom:1px solid var(--line)}
.login{left:87px;top:64px;font-size:12px;color:var(--muted);display:flex;align-items:center;gap:4px}
.brand{left:337px;top:40px;width:530px;height:60px;display:flex;align-items:center;justify-content:center;gap:14px}
.brand-dot{width:26px;height:26px;border-radius:50%;background:var(--rose)}
.brand-name{font-size:33px;font-weight:300;color:#666;letter-spacing:1px;text-transform:uppercase}
.cart{left:1042px;top:64px;font-size:12px;color:var(--muted);display:flex;gap:4px;align-items:center}

.main-nav{position:absolute;left:0;top:141px;width:1200px;height:54px;border-bottom:1px solid var(--line)}
.main-nav a{position:absolute;top:18px;font-size:12px;color:var(--muted);text-decoration:none;letter-spacing:.4px}
.main-nav a.active{color:var(--rose)}
.nav-underline{position:absolute;top:51px;height:2px;background:var(--rose)}
.nav-tool{position:absolute;top:14px}

/* hero */
.hero{left:87px;top:227px;width:699px;height:257px;background:linear-gradient(135deg,#eef4f8,#dfe9f0 60%,#e8eef2)}
.hero-ring{left:250px;top:-3px;width:262px;height:262px;border-radius:50%;background:#f5f5f5;box-shadow:0 4px 10px rgba(0,0,0,.18)}
.hero-title{left:250px;top:67px;width:262px;text-align:center;font-size:27px;font-weight:400;color:#333}
.hero-copy{left:255px;top:107px;width:252px;text-align:center;font-size:11px;font-weight:500;line-height:1.25;color:#333}
.hero .btn{left:310px;top:176px;width:136px;height:32px;border:1.5px solid #333;color:#333}

.section-title{position:absolute;text-align:center;font-weight:400;font-size:31px;letter-spacing:.5px}
.products-title{left:87px;top:512px;width:690px;color:#222}

/* product tiles */
.tile{position:absolute;width:345px;height:285px;color:#fff;text-align:center;overflow:hidden}
.tile h3{position:absolute;left:0;top:24px;width:100%;font-size:29px;font-weight:400;line-height:1.28;text-transform:uppercase;letter-spacing:.6px}
.tile .art{position:absolute;left:62px;top:138px;width:220px;height:120px;border-radius:10px;background:rgba(255,255,255,.16)}
.tile.two-line .art{top:130px}
.tile.three-line .art{top:168px;height:100px}
.teal{background:var(--teal)}
.blue{background:var(--blue)}
.pink{background:var(--pink)}
.tile.hover{background:var(--dark-teal)}
.tile.hover h3{text-transform:none;color:#6f8a86;font-size:29px;font-weight:300;top:20px}
.tile.hover .art{background:rgba(255,255,255,.06);top:150px}
.tile.hover .btn{left:81px;width:184px;height:32px;font-size:11px}
.btn.info{top:101px;background:var(--blue);color:#fff}
.btn.store{top:148px;background:transparent;border:1.5px solid #cfd8d6;color:#fff}
.tile.newsletter{background:var(--panel);color:var(--red)}
.tile.newsletter h3{font-size:31px;top:28px}
.tile.newsletter p{position:absolute;left:50px;top:120px;width:245px;font-size:11.5px;line-height:1.3;color:#555}
.tile.newsletter .btn{left:104px;top:218px;width:136px;height:32px;border:1.5px solid var(--red);color:var(--red);font-size:11px}

/* sidebar */
.member{left:797px;top:227px;width:317px;height:552px;border:1px solid var(--line)}
.member h2{position:absolute;left:0;top:30px;width:100%;text-align:center;font-size:31px;font-weight:400;line-height:1.15;color:var(--red)}
.member p{position:absolute;left:45px;top:118px;width:227px;text-align:center;font-size:11.5px;line-height:1.3;color:#555}
.member .btn{left:89px;top:207px;width:136px;height:32px;border:1.5px solid var(--red);color:var(--red);font-size:11px}
.member .art{position:absolute;left:30px;top:285px;width:257px;height:265px;border-radius:12px 12px 0 0;background:linear-gradient(180deg,#f3f6f9,#e4edf3)}

.news-title{left:797px;top:808px;width:317px;color:var(--red);font-weight:300}
.news-item{position:absolute;left:797px;width:317px;background:var(--panel);text-align:center}
.news-item.alt{background:var(--panel-alt)}
.news-date{margin-top:16px;font-size:18px;color:#222;display:flex;justify-content:center;align-items:center;gap:7px}
.news-item p{margin:8px auto 0;width:235px;font-size:11px;line-height:1.3;color:#555}
.btn.news-btn{left:887px;top:1422px;width:137px;height:32px;border:1.5px solid var(--blue);color:var(--blue);font-size:11px}
.rule{left:916px;top:1485px;width:77px;height:1px;background:#ccc}
.more-title{left:797px;top:1516px;width:317px;color:#222}

.stuff{position:absolute;width:159px;height:132px;color:#fff;display:flex;flex-direction:column;align-items:center;justify-content:flex-end;padding-bottom:20px;gap:12px;font-size:11.5px;font-weight:700;text-transform:uppercase}
.btn.shop{left:887px;top:1989px;width:137px;height:32px;border:1.5px solid #333;color:#333;font-size:11px}

/* footer */
.site-footer{left:0;top:2077px;width:1200px;height:222px;background:var(--footer);color:#999}
.disclaimer{position:absolute;left:87px;top:62px;width:765px;font-size:9.5px;line-height:1.3}
.disclaimer strong{color:var(--red)}
.payments{position:absolute;left:900px;top:66px;width:214px;display:flex;justify-content:space-between;align-items:center;font-weight:700;color:#8a8a8a}
.payments span{font-size:15px}
.payments small{font-size:9px;line-height:1;text-align:right}
.footer-rule{position:absolute;left:87px;top:141px;width:1027px;height:1px;background:#2c2c2c}
.footer-bar{position:absolute;left:87px;top:172px;font-size:11px;color:#aaa;display:flex;gap:12px}
.footer-links{position:absolute;left:354px;top:172px;font-size:11px;color:#ccc;display:flex;gap:12px}
.social{position:absolute;top:166px;width:24px;height:24px;border-radius:50%;background:#555}
</style>
</head>
<body>

<header class="site-header">
  <div class="abs login">LOGIN
    <svg width="10" height="11" viewBox="0 0 10 11"><rect x="1" y="5" width="8" height="6" fill="none" stroke="#34a6d7" stroke-width="1.2"/><path d="M3 5V3.5a2 2 0 0 1 4 0V5" fill="none" stroke="#34a6d7" stroke-width="1.2"/></svg>
  </div>
  <div class="abs brand"><span class="brand-dot"></span><span class="brand-name">allphonedeskhub.net</span></div>
  <div class="abs cart">CART (0)
    <svg width="13" height="11" viewBox="0 0 13 11"><path d="M0 1h2l2 6h7l1.5-4.5H3.3" fill="none" stroke="#34a6d7" stroke-width="1.2"/><circle cx="5" cy="9.5" r="1" fill="#34a6d7"/><circle cx="10" cy="9.5" r="1" fill="#34a6d7"/></svg>
  </div>
</header>

<nav class="main-nav">
  <a class="active" style="left:87px">HOME</a>
  <span class="nav-underline" style="left:87px;width:83px"></span>
  <a style="left:207px">STORE</a>
  <a style="left:328px">ABOUT US</a>
  <a style="left:475px">NEWS</a>
  <a style="left:593px">FREE STUFF</a>
  <a style="left:748px">MEMBERSHIP</a>
  <a style="left:916px">CONTACT US</a>
  <svg class="nav-tool" style="left:1061px" width="16" height="16" viewBox="0 0 16 16"><circle cx="12" cy="3" r="2" fill="#886aae"/><circle cx="4" cy="8" r="2" fill="#886aae"/><circle cx="12" cy="13" r="2" fill="#886aae"/><path d="M12 3 4 8l8 5" fill="none" stroke="#886aae" stroke-width="1.2"/></svg>
  <span class="nav-underline" style="left:1057px;width:26px;background:#886aae"></span>
  <svg class="nav-tool" style="left:1098px" width="16" height="16" viewBox="0 0 16 16"><circle cx="6.5" cy="6.5" r="5" fill="none" stroke="#f04a51" stroke-width="1.5"/><path d="m10.5 10.5 4 4" stroke="#f04a51" stroke-width="1.5"/></svg>
  <span class="nav-underline" style="left:1093px;width:26px;background:#f04a51"></span>
</nav>

<section class="abs hero" role="img" aria-label="Network of connected circles showing call centre agents, a cart and a computer">
  <div class="abs hero-ring"></div>
  <h1 class="abs hero-title">MARKET PLACE</h1>
  <p class="abs hero-copy">Where people who work in call centres can come and purchase downloadable templates, tool-kits, courseware etc to help them in their jobs</p>
  <span class="btn">Shop now</span>
</section>

<h2 class="section-title products-title">OUR PRODUCTS</h2>

<article class="tile teal three-line" style="left:87px;top:573px">
  <h3>Performance<br>Measurement &amp;<br>Management</h3>
  <div class="art" role="img" aria-label="Agent with headset between gears"></div>
</article>
<article class="tile hover" style="left:441px;top:573px">
  <div class="art" role="img" aria-label="Faded keys tagged with ideas"></div>
  <h3>Morale and<br>Motivation</h3>
  <span class="btn info">Product info</span>
  <span class="btn store">Store</span>
</article>

<article class="tile teal two-line" style="left:87px;top:869px">
  <h3>Reward and<br>Recognition</h3>
  <div class="art" role="img" aria-label="Agent sending a message across a globe"></div>
</article>
<article class="tile blue two-line" style="left:441px;top:869px">
  <h3>Morale and<br>Motivation</h3>
  <div class="art" role="img" aria-label="Agent at a laptop with a speech bubble"></div>
</article>

<article class="tile blue two-line" style="left:87px;top:1165px">
  <h3>Coaching and<br>Mentoring</h3>
  <div class="art" role="img" aria-label="Agent at a desk with speech bubbles and a globe"></div>
</article>
<article class="tile blue two-line" style="left:441px;top:1165px">
  <h3>Communication<br>Skills</h3>
  <div class="art" role="img" aria-label="Agent with headset and a speech bubble"></div>
</article>

<article class="tile pink two-line" style="left:87px;top:1461px">
  <h3>Call Centre<br>Technology</h3>
  <div class="art" role="img" aria-label="Computer, keyboard, cloud and documents"></div>
</article>
<article class="tile pink two-line" style="left:441px;top:1461px">
  <h3>Call Centre<br>Strategy</h3>
  <div class="art" role="img" aria-label="Gears inside a circular badge"></div>
</article>

<article class="tile pink two-line" style="left:87px;top:1756px">
  <h3>Research and<br>Best Practices</h3>
  <div class="art" role="img" aria-label="Magnifying glass linked to research icons"></div>
</article>
<article class="tile newsletter" style="left:441px;top:1756px">
  <h3>Join our<br>Newsletter</h3>
  <p>Ut wisi enim ad minim veniam, quis nostrud exerci tation ullamcorper suscipit lobortis nisl ut aliquip ex ea commodo consequat.</p>
  <span class="btn">Subscribe</span>
</article>

<aside class="abs member">
  <h2>BECOME A<br>MEMBER NOW!</h2>
  <p>Ut wisi enim ad minim veniam, quis nostrud exerci tation ullamcorper suscipit lobortis nisl ut aliquip ex ea commodo consequat.</p>
  <span class="btn">Sign up</span>
  <div class="art" role="img" aria-label="Call centre agent surrounded by work icons"></div>
</aside>

<h2 class="section-title news-title">LATEST NEWS</h2>
<div class="news-item" style="top:864px;height:129px">
  <div class="news-date">16 DEC <svg width="17" height="14" viewBox="0 0 17 14"><rect x=".75" y=".75" width="15.5" height="12.5" fill="none" stroke="#333" stroke-width="1.5"/><path d="M3 4h5M3 7h11M3 10h11M10 4h4" stroke="#333" stroke-width="1.4"/></svg></div>
  <p>Ut wisi enim ad minim veniam, quis nostrud exerci tation ullamcorper suscipit lobortis nisl ut aliquip ex ea commodo consequat.</p>
</div>
<div class="news-item alt" style="top:998px;height:128px">
  <div class="news-date">16 DEC <svg width="17" height="14" viewBox="0 0 17 14"><rect x=".75" y=".75" width="15.5" height="12.5" fill="none" stroke="#333" stroke-width="1.5"/><path d="M3 4h5M3 7h11M3 10h11M10 4h4" stroke="#333" stroke-width="1.4"/></svg></div>
  <p>Ut wisi enim ad minim veniam, quis nostrud exerci tation ullamcorper suscipit lobortis nisl ut aliquip ex ea commodo consequat.</p>
</div>
<div class="news-item" style="top:1131px;height:129px">
  <div class="news-date">16 DEC <svg width="17" height="14" viewBox="0 0 17 14"><rect x=".75" y=".75" width="15.5" height="12.5" fill="none" stroke="#333" stroke-width="1.5"/><path d="M3 4h5M3 7h11M3 10h11M10 4h4" stroke="#333" stroke-width="1.4"/></svg></div>
  <p>Ut wisi enim ad minim veniam, quis nostrud exerci tation ullamcorper suscipit lobortis nisl ut aliquip ex ea commodo consequat.</p>
</div>
<div class="news-item alt" style="top:1264px;height:131px">
  <div class="news-date">16 DEC <svg width="17" height="14" viewBox="0 0 17 14"><rect x=".75" y=".75" width="15.5" height="12.5" fill="none" stroke="#333" stroke-width="1.5"/><path d="M3 4h5M3 7h11M3 10h11M10 4h4" stroke="#333" stroke-width="1.4"/></svg></div>
  <p>Ut wisi enim ad minim veniam, quis nostrud exerci tation ullamcorper suscipit lobortis nisl ut aliquip ex ea commodo consequat.</p>
</div>
<span class="btn news-btn">News center</span>

<div class="abs rule"></div>
<h2 class="section-title more-title">MORE STUFF</h2>

<div class="stuff" style="left:797px;top:1572px;background:var(--red)">
  <svg width="58" height="44" viewBox="0 0 58 44" fill="none" stroke="#fff" stroke-width="2.5"><rect x="2" y="2" width="54" height="40" rx="2"/><path d="M2 10h54M2 34h54M23 15v14l12-7z"/></svg>Videos</div>
<div class="stuff" style="left:956px;top:1572px;background:var(--orange)">
  <svg width="50" height="48" viewBox="0 0 50 48" fill="none" stroke="#fff" stroke-width="2.5"><rect x="12" y="2" width="36" height="44"/><rect x="2" y="10" width="22" height="26" fill="#f68e4e"/><path d="M9 30V16h5a4 4 0 0 1 0 8H9M30 14a8 8 0 1 0 8 8h-8z"/></svg>Presentations</div>
<div class="stuff" style="left:797px;top:1704px;background:var(--purple)">
  <svg width="50" height="46" viewBox="0 0 50 46" fill="none" stroke="#fff" stroke-width="2.5"><rect x="10" y="2" width="30" height="12"/><rect x="2" y="14" width="46" height="20" rx="2"/><rect x="10" y="28" width="30" height="16"/><path d="M15 34h20M15 39h20"/></svg>Templates</div>
<div class="stuff" style="left:956px;top:1704px;background:var(--yellow)">
  <svg width="40" height="48" viewBox="0 0 40 48" fill="none" stroke="#fff" stroke-width="2.5"><path d="M6 2h32v40H8a4 4 0 0 1-4-4V6a4 4 0 0 1 4-4zM4 38a4 4 0 0 1 4-4h30"/><rect x="12" y="9" width="18" height="10"/></svg>Documents</div>
<div class="stuff" style="left:797px;top:1836px;background:var(--blue)">
  <svg width="46" height="48" viewBox="0 0 46 48" fill="none" stroke="#fff" stroke-width="2.5"><path d="M10 4 36 2l6 40-26 4z"/><path d="M16 12l16-1M17 18l16-1M17 24l16-1M18 30l16-1M18 36l10-1"/></svg>White papers</div>
<div class="stuff" style="left:956px;top:1836px;background:var(--teal)">
  <svg width="58" height="44" viewBox="0 0 58 44" fill="none" stroke="#fff" stroke-width="2.5"><path d="M29 8C22 3 12 3 4 5v34c8-2 18-2 25 3 7-5 17-5 25-3V5c-8-2-18-2-25 3zM29 8v34M10 14h13M10 20h13M10 26h13M35 14h13M35 20h13M35 26h13"/></svg>Other courses</div>

<span class="btn shop">Shop now!</span>

<footer class="abs site-footer">
  <p class="disclaimer"><strong>DISCLAIMER:</strong> Lorem ipsum dolor sit amet, consectetuer adipiscing elit, sed diam nonummy nibh euismod tincidunt ut laoreet dolore magna aliquam erat volutpat. Ut wisi enim ad minim veniam, quis nostrud exerci tation ullamcorper suscipit lobortis nisl ut aliquip ex ea commodo consequat. Duis autem vel eum iriure dolor in hendrerit in vulputate velit esse molestie consequat, vel illum dolore eu feugiat nulla facilisis at vero eros et accumsan et iusto odio dignissim qui blandit praesent luptatum zzril delenit augue duis dolore te feugait nulla facilisi.</p>
  <div class="payments"><span>Paivlo</span><span>KREDVIX</span><small>WIRE<br>TRANSFER</small></div>
  <div class="footer-rule"></div>
  <div class="footer-bar">Copyright 2015. All Rights Reserved.</div>
  <div class="footer-links"><span>PRIVACY POLICY</span><span>|</span><span>SITE MAP</span><span>|</span><span>CONTACT US</span></div>
  <span class="social" style="left:1024px"></span>
  <span class="social" style="left:1056px"></span>
  <span class="social" style="left:1088px"></span>
</footer>

</body>
</html>
```